Bright Harbor Brochure/Flyer Revisions

Improve the current design and over all look for Tri-Fold brochure and 8 x 11 flyer along with update the text and view picture substitutions.

Target Market(s)

Currently our brochure is geared more towards the Cancer Patient, and less Senior.
I want to take the new revisions text, or new message, and incorporate it into the new designed brochure and flyer. I want a nice picture of a senior or couple to be primary view shot and the cancer patients secondary.
Please visit our website; www.brightharbors.org

Requirements
Must have
• we want all Seniors and Cancer Patients that own a life insurance policy, group or individual to call us. We want the consumer to be educated and know their rights.
Bright Harbors will be there ADVOCATE and Financial RESOURCE

```html
<!DOCTYPE html>
<html lang="en">
<head>
<meta charset="utf-8">
<title>Bright Harbors Tri-Fold Brochure</title>
<link href="https://fonts.googleapis.com/css2?family=Questrial&family=Montserrat:wght@700;800&display=swap" rel="stylesheet">
<style>
  :root{
    --bg:#d9d9d9;
    --magenta:#a7327f;
    --magenta-deep:#8e2a78;
    --blue:#3d78b0;
    --blue-deep:#2f5f95;
    --green:#2f6a36;
    --green-dark:#1f4a27;
    --brown:#5a3a2a;
    --paper:#efefef;
    --white:#ffffff;
    --ink:#2b4f8a;
  }
  *{box-sizing:border-box;margin:0;padding:0}
  html,body{width:1200px;height:1000px;overflow:hidden}
  body{background:var(--bg);font-family:"Questrial",sans-serif;position:relative}
  .brochure{position:absolute;left:75px;top:150px;width:1050px;height:700px;display:flex;box-shadow:0 10px 30px rgba(0,0,0,.25)}
  .panel{position:relative;width:350px;height:100%;overflow:hidden}

  /* left panel */
  .panel--cover .photo{position:absolute;inset:0;background:linear-gradient(160deg,#c9b2a2 0%,#a9a3a7 45%,#8f97a6 75%,#b4b9c2 100%)}
  .discover{position:absolute;left:0;top:360px;width:300px}
  .discover__title{display:inline-block;background:var(--white);color:var(--magenta);font-family:"Montserrat",sans-serif;font-weight:800;font-size:34px;padding:4px 60px 2px 18px}
  .discover__body{background:var(--magenta);color:var(--white);font-size:15px;line-height:1.3;padding:14px 18px 20px}

  /* middle panel */
  .panel--contact .foliage{position:absolute;left:0;top:0;width:100%;height:300px;background:linear-gradient(180deg,#4e7d3f,#2f5e2d 60%,#47713f)}
  .foliage__text{position:absolute;left:30px;top:150px;right:26px;color:var(--white);font-size:14.5px;line-height:1.3}
  .callbox{position:absolute;left:0;top:300px;width:100%;height:330px;background:linear-gradient(180deg,var(--blue),var(--blue-deep))}
  .callbox__lead{position:absolute;left:60px;top:12px;color:var(--white);font-size:14px;letter-spacing:2px}
  .callbox__phone{position:absolute;left:40px;top:36px;background:var(--white);color:var(--blue);border-radius:18px;padding:6px 22px;font-size:30px;letter-spacing:3px}
  .brand{position:absolute;right:18px;top:90px;display:flex;align-items:center;gap:6px;color:var(--white);font-size:13px}
  .brand__dot{width:12px;height:12px;border-radius:50%;background:var(--white)}
  .callbox__body{position:absolute;left:32px;right:28px;top:120px;color:var(--white);font-size:14.5px;line-height:1.3}
  .contact-strip{position:absolute;left:0;bottom:0;width:100%;height:70px;background:var(--paper);display:flex;align-items:center;padding-left:40px;gap:10px;color:var(--blue);font-size:19px}
  .social{width:22px;height:22px;border-radius:50%;background:var(--blue)}

  /* right panel */
  .panel--message .top-green{position:absolute;left:0;top:0;width:100%;height:150px;background:var(--green)}
  .panel--message .top-brown{position:absolute;left:0;top:150px;width:100%;height:150px;background:linear-gradient(180deg,var(--brown),#6a4a3a)}
  .message{position:absolute;left:0;top:300px;width:100%;height:330px;background:linear-gradient(180deg,#b3478c,var(--magenta-deep))}
  .inset-photo{position:absolute;left:120px;top:210px;width:130px;height:130px;border-radius:50%;border:6px solid #cfd3da;background:radial-gradient(circle at 40% 40%,#5f86c4,#2e4f8d)}
  .message__head{position:absolute;left:28px;top:50px;color:var(--white);font-family:"Montserrat",sans-serif;font-weight:800;font-size:22px;letter-spacing:.5px}
  .message__sub{position:absolute;left:60px;top:78px;color:var(--white);font-size:12.5px}
  .message__quote{position:absolute;left:60px;top:96px;color:var(--white);font-family:"Montserrat",sans-serif;font-weight:800;font-size:30px}
  .message__body{position:absolute;left:30px;right:24px;top:146px;color:var(--white);font-size:14.5px;line-height:1.3}
  .web-strip{position:absolute;left:0;bottom:0;width:100%;height:70px;background:var(--paper);display:flex;align-items:center;justify-content:center;color:var(--magenta);font-size:18px;letter-spacing:3px}
</style>
</head>
<body>
<div class="brochure">

  <section class="panel panel--cover">
    <div class="photo" role="img" aria-label="Photograph of a patient in a headscarf looking down thoughtfully"></div>
    <div class="discover">
      <h2 class="discover__title">Discover</h2>
      <p class="discover__body">Why do insurance companies conceal the fact that policy holders may be entitled to additional cash benefits? Why are bankruptcy rates among cancer patients and seniors more than double than that of the general population? Why do patients without financial stress</p>
    </div>
  </section>

  <section class="panel panel--contact">
    <div class="foliage" role="img" aria-label="Soft green foliage background photograph"></div>
    <p class="foliage__text">Why do insurance companies conceal the fact that policy holders may be entitled to additional cash benefits? Why are bankruptcy rates among cancer patients and seniors more than double than</p>
    <div class="callbox">
      <p class="callbox__lead">Give Us a call with</p>
      <p class="callbox__phone">800-555-0142</p>
      <div class="brand"><span class="brand__dot"></span><span>Bright Harbors</span></div>
      <p class="callbox__body">Why do insurance companies conceal the fact that policy holders may be entitled to additional cash benefits? Why are bankruptcy rates among cancer patients and seniors more than double than that of the general population? Why do patients without financial stress have significantly faster improvement rates over time in functional, emotional, and physical well-being as compared with patients who faced economic burdens?</p>
    </div>
    <div class="contact-strip">
      <span>Contact us via.</span>
      <span class="social"></span><span class="social"></span><span class="social"></span>
    </div>
  </section>

  <section class="panel panel--message">
    <div class="top-green"></div>
    <div class="top-brown"></div>
    <div class="message">
      <h2 class="message__head">HEALING &amp; RECOVERY</h2>
      <p class="message__sub">should be the primary concern for all patients</p>
      <p class="message__quote">“NOT MONEY”</p>
      <p class="message__body">Why do insurance companies conceal the fact that policy holders may be entitled to additional cash benefits? Why are bankruptcy rates among cancer patients and seniors more than double than that of the general population? Why do patients without financial stress have significantly faster improvement rates over time in functional, emotional, and physical well-being as compared with patients who faced economic burdens?</p>
    </div>
    <div class="inset-photo" role="img" aria-label="Round photograph of a caregiver holding a senior's hands"></div>
    <div class="web-strip">www.brightharbors.org</div>
  </section>

</div>
</body>
</html>
```